Brightfold Reach - B2B Demand Generation Website Project

We need a fully functional website for www.brightfoldreach-example.com. We are a B2B Demand Generation company, based in London, working with companies such as QTR, DWN, Vortan, Brelloway, Pelta generating them sales leads for their sales teams. We run this through digital marketing newsletter promotions and have a network of websites. Content syndication, data, demand generation, online marketing. Our logo has just been redone (attached) and we have a holding page already which i would like to use the style / colours. Our logo is bright and vibrant but i dont want the site to be a rainbow. We are expensive, classy, professorial, B2B, intelligent.

Home
About Us
Our Services
Prospero & QA Technology
Intent Data
Testimonials
Contact Us

Target Market(s)

B2B Marketers (QTR, Quorvane, Pelta, DWN, Vista Hub, Harrowby, Tremont Axis, Technology Companies, Data Companies, Marketing Teams, Cloudwick.

Industry/Entity Type

Marketing

Coding

Coded - Design and coding required

Number of Pages Required

5+ page

Font styles to use
Sans Serif

Requirements
Must have
• Home
About Us
Our Services
Prospero & QA Technology
Intent Data
Testimonials
Contact Us

Simple Pages.

Look classy, intelligent, data experts. I like the video homepages were the image moves at the top. Very soft animation.
Nice to have
• Websites i like:

https://www.dwn-example.com/
https://www.pulsegate-example.com/
https://www.lmsitecraft-example.co.uk/

Brightfold Reach - The Demand Generation Company
Should not have
• Pixelvault crap images

```html
<!DOCTYPE html>
<html lang="en">
<head>
<meta charset="utf-8">
<title>Brightfold Reach - The Demand Generation Company</title>
<link href="https://fonts.googleapis.com/css2?family=Poppins:wght@400;500;600;700;800&family=Libre+Baskerville&display=swap" rel="stylesheet">
<style>
:root{
  --red:#d2232a;
  --navy:#17478c;
  --footer:#1d4fa2;
  --ink:#1b1b1b;
  --grey-bg:#dcdcdc;
  --text:#333;
  --white:#fff;
  --line:#d6d6d6;
}
*{box-sizing:border-box;margin:0;padding:0}
html,body{width:1200px;height:3853px;overflow:hidden}
body{font-family:"Poppins",sans-serif;color:var(--text);position:relative;background:var(--white)}
.abs{position:absolute}
.btn{display:inline-block;background:var(--red);color:var(--white);font-size:11px;font-weight:700;padding:6px 10px;letter-spacing:.3px}
.sec-title{position:absolute;left:0;width:1200px;text-align:center;font-weight:800;font-size:29px;color:var(--ink);letter-spacing:-.3px}
.sec-title::after{content:"";display:block;width:38px;height:3px;background:var(--red);margin:14px auto 0}

/* hero */
.hero{left:0;top:0;width:1200px;height:673px;background:radial-gradient(ellipse at 30% 45%,#0c2a55 0%,#0d3a78 25%,#1a6ac4 45%,#0a2448 70%,#040f22 100%)}
.brand{color:var(--white);text-align:center}
.brand-name{font-size:28px;font-weight:400;letter-spacing:-.5px;white-space:nowrap;line-height:34px}
.brand-tag{font-size:9px;color:#cfe0ff;white-space:nowrap}
.nav{top:30px;left:367px;display:flex;gap:0;font-size:13px;font-weight:500;color:var(--white)}
.nav span{padding:3px 10px}
.nav .active{background:var(--red)}
.hero-tag{left:960px;top:514px;color:var(--white);font-size:24px;line-height:30px;font-weight:400}
.hero-tag b{color:var(--red);font-weight:500;font-size:22px}
.dots{left:553px;top:624px;display:flex;gap:12px;align-items:center}
.dots i{width:8px;height:8px;border-radius:50%;background:#fff;display:block}
.dots i.on{width:14px;height:14px;background:var(--red);border:2px solid #fff}

/* services */
.services{left:0;top:673px;width:1200px;height:572px;background:var(--grey-bg)}
.card{position:absolute;top:141px;width:296px;height:376px;background:var(--white);text-align:center;padding:42px 30px 0}
.card h3{font-size:15px;font-weight:700;color:var(--ink);line-height:23px;margin:22px 0 20px}
.card p{font-size:12px;line-height:17.5px;color:#444;margin-bottom:22px}

/* welcome */
.welcome{left:0;top:1245px;width:1200px;height:501px}
.welcome-mark{left:150px;top:60px;width:410px;height:390px;display:flex;align-items:center;justify-content:center}
.welcome-mark span{font-size:40px;font-weight:600;color:var(--red)}
.welcome-copy{left:621px;top:75px;width:430px}
.welcome-copy h4{font-size:18px;font-weight:600;color:var(--ink)}
.welcome-copy h2{font-size:34px;font-weight:500;color:var(--ink);line-height:40px}
.welcome-copy h2::after{content:"";display:block;width:124px;height:3px;background:var(--red);margin:10px 0 42px}
.welcome-copy p{font-size:13.5px;line-height:21.5px;color:#333;margin-bottom:40px}

/* stats */
.stats{left:0;top:1746px;width:1200px;height:277px;background:var(--navy);display:flex;color:var(--white)}
.stat{flex:1;text-align:center;padding-top:60px;position:relative}
.stat+.stat{border-left:1px solid rgba(255,255,255,.2)}
.stat svg{width:56px;height:56px}
.stat .num{font-family:"Libre Baskerville",serif;font-size:22px;margin-top:24px}
.stat .num b{font-size:28px;font-weight:400}
.stat .lbl{font-size:14px;font-weight:600;margin-top:10px;letter-spacing:.3px}
.stats .stat:nth-child(1){flex:0 0 415px}
.stats .stat:nth-child(2){flex:0 0 382px}

/* qa */
.qa{left:0;top:2023px;width:1200px;height:531px;background:linear-gradient(100deg,#e8e6e2 0%,#f2f0ec 40%,#d9d6d0 70%,#c9c6c0 100%)}
.qa-card{left:94px;top:2150px;width:344px;height:333px;background:rgba(255,255,255,.96);padding:34px 32px}
.qa-card h2{font-size:25px;font-weight:800;color:var(--ink);margin-bottom:14px}
.qa-card p{font-size:14px;line-height:21.7px;color:#333;margin-bottom:22px}

/* partners */
.partner{position:absolute;width:175px;height:87px;border:1px solid var(--line);display:flex;align-items:center;justify-content:center;font-size:22px;font-weight:700;color:var(--navy)}

/* testimonials */
.testi{left:0;top:2988px;width:1200px;height:474px;background:var(--grey-bg)}
.tcard{position:absolute;top:145px;width:302px;height:272px;background:var(--white);padding:22px 24px}
.tcard .q{font-family:"Libre Baskerville",serif;font-size:34px;color:var(--navy);line-height:28px;font-weight:700}
.tcard p{font-size:11.5px;line-height:17.6px;color:#333;margin:8px 0 0 26px}
.tcard .who{display:flex;align-items:center;gap:10px;margin:26px 0 0 22px;font-size:11px;font-weight:700;color:var(--ink)}
.tcard .who small{font-weight:400;font-size:9px;color:#555}
.avatar{width:34px;height:34px;border-radius:50%;background:#c9ced6}
.arrow{position:absolute;top:268px;width:32px;height:32px;border-radius:50%;border:1px solid #777;display:flex;align-items:center;justify-content:center}

/* footer */
.footer{left:0;top:3462px;width:1200px;height:391px;background:linear-gradient(120deg,#1a4a9c,#1f55ad 55%,#1a4a9a);color:var(--white)}
.foot-col h5{font-size:14px;font-weight:700;letter-spacing:.4px;margin-bottom:22px}
.foot-menu li{list-style:none;font-size:12.5px;line-height:21.8px}
.contact-row{display:flex;gap:12px;font-size:12.5px;line-height:17px;margin-bottom:20px}
.ring{flex:0 0 26px;height:26px;border-radius:50%;background:var(--white);display:flex;align-items:center;justify-content:center}
.copy{left:0;top:375px;width:1200px;text-align:center;font-size:10px}
</style>
</head>
<body>

<!-- hero -->
<section class="abs hero" role="img" aria-label="Abstract blue data tunnel of glowing dots spiralling into the distance"></section>
<div class="abs brand" style="left:113px;top:22px;width:260px">
  <div style="width:50px;height:50px;border-radius:50%;border:2px solid #fff;margin:0 auto 12px"></div>
  <div class="brand-name">Brightfold Reach</div>
  <div class="brand-tag">The Demand Generation Company</div>
</div>
<nav class="abs nav">
  <span class="active">Home</span><span>About Us</span><span>Our Services</span><span>Prospero &amp; QA Technology</span><span>Intent Data</span><span>Testimonials</span><span>Contact Us</span>
</nav>
<div class="abs hero-tag"><b>Brightfold Reach</b><br>The Demand<br>Generation<br>Company</div>
<div class="abs dots"><i></i><i></i><i class="on"></i><i></i><i></i></div>

<!-- services -->
<section class="abs services">
  <h2 class="sec-title" style="top:50px">OUR SERVICES</h2>
  <article class="card" style="left:130px">
    <svg width="70" height="66" viewBox="0 0 70 66"><rect x="26" y="4" width="40" height="32" fill="none" stroke="#17478c" stroke-width="3"/><circle cx="12" cy="14" r="6" fill="#17478c"/><path d="M4 24h16l8 8v4h-8v26h-5V46h-2v16H8V36H4z" fill="#17478c"/><path d="M34 14h8v6h-8zM48 12h10v6H48zM48 24h10v6H48z" fill="none" stroke="#17478c" stroke-width="2"/><path d="M30 36l-6 24M60 36l6 24" stroke="#17478c" stroke-width="3"/></svg>
    <h3>MARKETING QUALIFIED<br>LEADS (MQL)</h3>
    <p>A Marketing Qualified Lead (MQL) is a prospect that has expressed an interest in what your brand has to offer.</p>
    <span class="btn">READ MORE</span>
  </article>
  <article class="card" style="left:452px">
    <svg width="70" height="66" viewBox="0 0 70 66"><rect x="18" y="2" width="48" height="48" fill="#17478c"/><path d="M40 2v48M18 26h48" stroke="#fff" stroke-width="3"/><circle cx="40" cy="14" r="5" fill="#fff"/><circle cx="30" cy="26" r="5" fill="#fff"/><path d="M2 48l14-10 8 6-6 20H6z" fill="#17478c"/></svg>
    <h3>ACCOUNT BASED<br>MARKETING LEADS (ABM)</h3>
    <p>ABM is a strategy that directs marketing resources to engaging a specific set of target accounts. Instead of casting a wide...</p>
    <span class="btn">READ MORE</span>
  </article>
  <article class="card" style="left:773px">
    <svg width="70" height="66" viewBox="0 0 70 66"><path d="M4 4v58h64" fill="none" stroke="#17478c" stroke-width="3"/><rect x="12" y="34" width="8" height="24" fill="#17478c"/><rect x="24" y="24" width="8" height="34" fill="#17478c"/><rect x="36" y="30" width="8" height="28" fill="#17478c"/><rect x="48" y="14" width="8" height="44" fill="#17478c"/><rect x="60" y="6" width="6" height="52" fill="#17478c"/></svg>
    <h3>SALES QUALIFIED<br>LEAD / BANT</h3>
    <p>An SQL lead or a BANT lead is a type of lead that expressed a specific interest in a product and service that you have to offer...</p>
    <span class="btn">READ MORE</span>
  </article>
</section>

<!-- welcome -->
<section class="abs welcome">
  <div class="abs welcome-mark"><span>Brightfold Reach</span></div>
  <div class="abs welcome-copy">
    <h4>Welcome to</h4>
    <h2>Brightfold Reach</h2>
    <p>Brightfold Reach offers multi-channel demand generation services to publishers and technology vendors through our network oz lead generation websites and native speaking telemarketing agents. Whether looking for MQL, ABM or BANT campaigns, Brightfold Reach can assist you in delivering your demand generation strategy and generate pipeline for your sales teams and/or channel partners.</p>
    <span class="btn">READ MORE</span>
  </div>
</section>

<!-- stats -->
<section class="abs stats">
  <div class="stat">
    <svg viewBox="0 0 56 56"><path d="M28 6v28M18 24l10 10 10-10" fill="none" stroke="#fff" stroke-width="5"/><path d="M6 34v16h44V34" fill="none" stroke="#fff" stroke-width="5"/></svg>
    <div class="num">Ticker to <b>70,000+</b></div>
    <div class="lbl">DOWNLOADS PER MONTH</div>
  </div>
  <div class="stat">
    <svg viewBox="0 0 56 56"><circle cx="28" cy="28" r="20" fill="none" stroke="#fff" stroke-width="3" stroke-dasharray="6 4"/><circle cx="28" cy="28" r="13" fill="none" stroke="#fff" stroke-width="3"/><path d="M22 22h12M22 28h12M22 34h12" stroke="#fff" stroke-width="2.5"/></svg>
    <div class="num">Ticker to <b>25,000+</b></div>
    <div class="lbl">LEADS DELIVERED PER MONTH</div>
  </div>
  <div class="stat">
    <svg viewBox="0 0 56 56"><circle cx="28" cy="28" r="24" fill="none" stroke="#fff" stroke-width="3"/><ellipse cx="28" cy="28" rx="11" ry="24" fill="none" stroke="#fff" stroke-width="3"/><path d="M4 28h48M8 16h40M8 40h40M28 4v48" stroke="#fff" stroke-width="3"/></svg>
    <div class="num">Ticker to <b>50+</b></div>
    <div class="lbl">COUNTRIES WE CAN REACH</div>
  </div>
</section>

<!-- qa technology -->
<section class="abs qa" role="img" aria-label="Hands typing on a laptop on a bright wooden desk with sticky notes"></section>
<div class="abs qa-card">
  <h2>QA TECHNOLOGY</h2>
  <p>Prospero is a proprietary lead verification platform from Brightfold Reach that aims to sift out invalid leads with questionable or erroneous data. The platform is designed to equip sales teams with accurate, high-quality records in order to improve lead generation, accelerate pipeline and increase revenue.</p>
  <span class="btn">READ MORE</span>
</div>

<!-- partners -->
<h2 class="sec-title" style="top:2618px">WHO WE WORK WITH</h2>
<div class="partner" style="left:130px;top:2729px">QTR</div>
<div class="partner" style="left:322px;top:2729px">Pelta</div>
<div class="partner" style="left:513px;top:2729px;font-size:17px">DWN Enterprise</div>
<div class="partner" style="left:704px;top:2729px">Korvell</div>
<div class="partner" style="left:895px;top:2729px">Cloudnest</div>
<div class="partner" style="left:130px;top:2830px">Orvane</div>
<div class="partner" style="left:322px;top:2830px">Shiftwell</div>
<div class="partner" style="left:513px;top:2830px">Cytrel</div>
<div class="partner" style="left:704px;top:2830px">Marquell</div>

<!-- testimonials -->
<section class="abs testi">
  <h2 class="sec-title" style="top:34px">TESTIMONIALS</h2>
  <div class="arrow" style="left:67px"><svg width="10" height="10" viewBox="0 0 10 10"><path d="M7 1L3 5l4 4" fill="none" stroke="#333" stroke-width="1.6"/></svg></div>
  <div class="arrow" style="left:1096px"><svg width="10" height="10" viewBox="0 0 10 10"><path d="M3 1l4 4-4 4" fill="none" stroke="#333" stroke-width="1.6"/></svg></div>
  <article class="tcard" style="left:130px">
    <div class="q">&ldquo;</div>
    <p>Lorem ipsum dolor sit amet, conse ctetur adipiscing elit, sed do eiusmod tempor incididunt ut labore et dolore magna aliqua. Ut enim ad minim veniam, quis nostrud exercitation ullamco laboris nisi ut aliquip ex ea commodo consequat. Duis aute irure dolor in reprehenderit.</p>
    <div class="who"><span class="avatar"></span>DORIAN <small>Sydney</small></div>
  </article>
  <article class="tcard" style="left:449px">
    <div class="q">&ldquo;</div>
    <p>Lorem ipsum dolor sit amet, conse ctetur adipiscing elit, sed do eiusmod tempor incididunt ut labore et dolore magna aliqua. Ut enim ad minim veniam, quis nostrud exercitation ullamco laboris nisi ut aliquip ex ea commodo consequat. Duis aute irure dolor in reprehenderit.</p>
    <div class="who"><span class="avatar"></span>DORIAN <small>Sydney</small></div>
  </article>
  <article class="tcard" style="left:769px">
    <div class="q">&ldquo;</div>
    <p>Lorem ipsum dolor sit amet, conse ctetur adipiscing elit, sed do eiusmod tempor incididunt ut labore et dolore magna aliqua. Ut enim ad minim veniam, quis nostrud exercitation ullamco laboris nisi ut aliquip ex ea commodo consequat. Duis aute irure dolor in reprehenderit.</p>
    <div class="who"><span class="avatar"></span>DORIAN <small>Sydney</small></div>
  </article>
</section>

<!-- footer -->
<footer class="abs footer">
  <div class="abs brand" style="left:110px;top:70px;width:340px">
    <div style="width:60px;height:60px;border-radius:50%;border:2px solid #fff;margin:0 auto 14px"></div>
    <div class="brand-name" style="font-size:34px;line-height:42px">Brightfold Reach</div>
    <div class="brand-tag" style="font-size:11px">The Demand Generation Company</div>
  </div>
  <div class="abs foot-col" style="left:491px;top:70px">
    <h5>MENU</h5>
    <ul class="foot-menu"><li>HOME</li><li>ABOUT US</li><li>OUR SERVICES</li><li>PROSPERO &amp; QA TECHNOLOGY</li><li>INTENT DATA</li><li>TESTIMONIALS</li><li>CONTACT US</li></ul>
  </div>
  <div class="abs foot-col" style="left:703px;top:70px;width:250px">
    <h5>CONTACT US</h5>
    <div class="contact-row"><span class="ring"><svg width="12" height="14" viewBox="0 0 12 14"><path d="M6 0a5 5 0 015 5c0 4-5 9-5 9S1 9 1 5a5 5 0 015-5z" fill="#1d4fa2"/><circle cx="6" cy="5" r="2" fill="#fff"/></svg></span><span>Harbour Court, 14 Mill Lane,<br>Eastbridge EB4 2KT</span></div>
    <div class="contact-row"><span class="ring"><svg width="12" height="12" viewBox="0 0 12 12"><path d="M2 0l3 3-1.5 2a7 7 0 003.5 3.5L9 7l3 3-2 2C5 12 0 7 0 2z" fill="#1d4fa2"/></svg></span><span>Call Us<br>555.010.0199</span></div>
    <div class="contact-row"><span class="ring"><svg width="12" height="10" viewBox="0 0 12 10"><rect width="12" height="10" fill="#1d4fa2"/><path d="M0 0l6 5 6-5" fill="none" stroke="#fff" stroke-width="1.2"/></svg></span><span style="font-size:11.5px">E mail Us<br>info@brightfoldreach-example.com</span></div>
  </div>
  <div class="abs foot-col" style="left:960px;top:70px;width:150px">
    <h5>FOLLOW US</h5>
    <div class="contact-row"><span class="ring"></span><span>Like us on<br>FRIENDLOOP</span></div>
    <div class="contact-row"><span class="ring"></span><span>Follow us on<br>CHIRPER</span></div>
    <div class="contact-row"><span class="ring"></span><span>Follow us on<br>LINKHALL</span></div>
  </div>
  <div class="abs copy">Copyright &copy; 2020 All Rights Reserved</div>
</footer>

</body>
</html>
```